Advertising Portal Needs eBrochure

Hi Crowders! Our advertising portal, which focus on the new launches property, needs an online brochure to promote to potential advertisers the benefits of advertising their projects with us. These advertisers will be mainly real estate developers and agencies.

WHAT WE LOOKING FOR
We do not want over-fanciful designs that makes the content hard to read. The use of illustrations and graphics/symbols related to covered topics are encouraged. The overall design should portrait our advertising efficiency through online and social media means. Our website - www.brightkeyhomes.sg.

For draft purposes, just do up the front page, back page, and few inner pages, preferably to include one illustration chart (either on page 7/8). Size wise probably A5 portrait or landscape, for future printing into a booklet.

WORK COMPLETION AND PAYMENT
The $500 stated here is 50% of the payment. Upon getting a desired draft design, we will need you to work on the full content with slight amendments along the way. Once done, we will be paying the balance $500, and we will need the pdf file as well as the work file.

Let your design juice flow, and hope we can work with you!
Updates

Hi Crowders! Thank you for your submissions. We are closing the project as we've decided on a design. It's a pity we can only select one design, as there are a number of good works. Hope we will have a chance to work together on our upcoming projects. Cheers =)

Target Market(s)

Real estate developers, real estate agencies, and perhaps to an extent, individual property sales agent.

Industry/Entity Type

Advertising

Requirements
Should not have
• We prefer not to have much real people kind of stock images. Try not to use images from our portal as we do not have the ownerships. Instead, you can use stock images of property developments artist impression that gives a similar feel.

```html
<!DOCTYPE html>
<html lang="en">
<head>
<meta charset="utf-8">
<title>Bright Key Homes – Marketing Packages eBrochure</title>
<link rel="stylesheet" href="https://fonts.googleapis.com/css2?family=Open+Sans:wght@400;600;700&family=Roboto+Condensed:wght@300;400;700&display=swap">
<style>
  :root{
    --green:#17905f;
    --green-dark:#0e7a4e;
    --green-bright:#3fbf4f;
    --green-row:#2fa94a;
    --green-soft:#5fd06a;
    --teal:#2bb3a0;
    --orange:#f18a1d;
    --orange-dark:#d9740c;
    --red:#e5473b;
    --yellow:#f5c21b;
    --blue:#3a9fd8;
    --paper:#ffffff;
    --grey:#eeeeee;
    --ink:#333333;
    --label:#222222;
    --stage:#ffffff;
  }
  *{box-sizing:border-box;margin:0;padding:0}
  html,body{width:900px;height:1200px;overflow:hidden;background:var(--stage)}
  body{font-family:"Open Sans",Arial,sans-serif;color:var(--ink)}
  .stage{position:relative;width:900px;height:1200px;overflow:hidden}

  .view-label{position:absolute;font-family:"Roboto Condensed",Arial,sans-serif;font-weight:300;color:var(--label)}
  .view-label--top{left:60px;top:22px;font-size:30px}
  .view-label--cover{left:560px;top:585px;font-size:40px}
  .view-label--bottom{left:360px;top:1100px;font-size:30px}

  .spread{position:absolute;display:flex;box-shadow:0 6px 18px rgba(0,0,0,.18)}
  .spread--campaign{left:50px;top:75px}
  .spread--steps{left:50px;top:790px}
  .page{position:relative;width:400px;height:283px;overflow:hidden}
  .spread .page:first-child::after{content:"";position:absolute;right:0;top:0;width:14px;height:100%;background:linear-gradient(90deg,rgba(0,0,0,0),rgba(0,0,0,.12))}

  .heading{font-family:"Roboto Condensed",Arial,sans-serif;font-weight:700;text-transform:uppercase;line-height:1.05}
  .body-text{font-size:5.6px;line-height:1.45}

  /* campaign page */
  .page--campaign{background:var(--green);color:#fff;padding:22px 22px}
  .step-title{display:flex;gap:7px;align-items:flex-start}
  .step-num{background:var(--red);color:#fff;font-family:"Roboto Condensed",Arial,sans-serif;font-weight:700;font-size:18px;width:20px;height:24px;display:flex;align-items:center;justify-content:center;flex:none}
  .step-title .heading{font-size:13px;color:#fff}
  .page--campaign .body-text{margin-top:7px;width:60%;color:#e6f5ee}
  .page--campaign .sub-heading{font-family:"Roboto Condensed",Arial,sans-serif;font-weight:700;font-size:9px;margin-top:10px;text-transform:uppercase}
  .callout{margin-top:8px;width:60%;background:var(--teal);border-radius:3px;padding:5px 7px;font-size:5.6px;line-height:1.45;font-style:italic}
  .ribbon-art{position:absolute;right:0;top:95px;width:170px;height:140px;background:linear-gradient(160deg,#31b9a6 0%,#f0c43a 45%,#e5473b 70%,#7b4fb0 100%);opacity:.9;border-radius:60px 0 0 0}

  /* results page */
  .page--results{background:var(--paper);padding-top:16px}
  .results-band{background:var(--green-dark);color:#fff;padding:6px 18px 4px}
  .results-band .heading{font-size:11px;color:#ffd54a;text-transform:none}
  .results-table{width:100%;border-collapse:collapse;font-size:6.2px;color:#fff}
  .results-table caption{caption-side:top;text-align:left;background:var(--green-dark);color:#fff;font-weight:700;font-size:7px;padding:3px 18px}
  .results-table th,.results-table td{padding:3px 18px;text-align:left;font-style:italic;border-top:1px solid rgba(255,255,255,.45)}
  .results-table th{font-weight:600;background:var(--green-row)}
  .results-table td{background:var(--green-bright)}
  .results-table tr:nth-child(even) td{background:var(--green-row)}
  .results-note{padding:5px 18px 0;font-size:5.6px;font-style:italic;font-weight:700}
  .see-it{padding:2px 18px 0;font-family:"Roboto Condensed",Arial,sans-serif;font-weight:700;font-size:10px;color:var(--green)}
  .page--results .body-text{padding:2px 18px 0}
  .page--results .body-text strong{color:var(--green-dark)}

  /* cover */
  .page--cover{position:absolute;left:120px;top:425px;box-shadow:0 6px 18px rgba(0,0,0,.18);background:var(--green)}
  .cover-head{height:85px;background:linear-gradient(180deg,#fafafa,#e3e3e3);display:flex;flex-direction:column;align-items:center;justify-content:center}
  .brand{display:flex;align-items:center;gap:6px;font-family:"Open Sans",Arial,sans-serif;font-weight:700;font-size:25px;color:var(--green);letter-spacing:-.5px}
  .brand-mark{width:18px;height:18px;border-radius:50%;background:var(--green)}
  .brand-tagline{font-size:5.2px;letter-spacing:1.5px;color:#777;margin-top:2px}
  .cover-title{position:absolute;left:30px;top:112px;color:#fff;font-size:29px;width:170px}
  .cover-sub{position:absolute;left:30px;top:178px;width:160px;background:var(--green-soft);color:#fff;font-family:"Roboto Condensed",Arial,sans-serif;font-size:9px;line-height:1.1;padding:4px 6px;text-transform:uppercase}
  .cover-art{position:absolute;right:22px;top:100px;width:170px;height:150px;border-radius:50%;background:radial-gradient(circle,#2f9f78 0%,#1b8a60 60%,rgba(23,144,95,0) 72%)}
  .cover-contact{position:absolute;left:30px;bottom:14px;right:30px;display:flex;justify-content:space-between;font-size:4.8px;color:#cfeede;line-height:1.5}

  /* about page */
  .page--about{background:var(--paper)}
  .icon-grid{position:absolute;left:14px;top:14px;width:200px;height:130px}
  .tile{position:absolute;width:40px;height:40px;display:flex;flex-direction:column;align-items:center;justify-content:flex-end;padding-bottom:3px;font-family:"Roboto Condensed",Arial,sans-serif;font-size:4.6px;color:#fff;text-transform:uppercase}
  .tile svg{margin-bottom:3px}
  .tile--target{left:50px;top:10px;background:#8dc63f}
  .tile--mobile{left:110px;top:0;background:var(--red)}
  .tile--idea{left:0;top:85px;background:#4fc3e8}
  .tile--schedule{left:55px;top:68px;background:var(--orange)}
  .tile--planning{left:110px;top:70px;background:var(--blue)}
  .tile--growth{left:160px;top:40px;background:var(--orange)}
  .about-block{position:absolute;left:150px;top:150px;width:230px}
  .about-block .heading{font-size:20px;color:var(--green)}
  .tag{display:inline-block;font-family:"Roboto Condensed",Arial,sans-serif;font-size:6.5px;color:#fff;padding:1px 5px;margin-left:4px;vertical-align:middle;text-transform:uppercase}
  .tag--green{background:var(--green-bright)}
  .tag--orange{background:var(--orange)}
  .how-block{position:absolute;left:40px;top:205px;width:240px}
  .how-block .heading{font-size:20px;color:var(--orange)}
  .about-block .body-text,.how-block .body-text{margin-top:3px;color:#555}

  /* steps page */
  .page--steps{background:var(--orange);color:#fff}
  .steps-title{position:absolute;left:18px;top:18px;font-size:24px;width:90px}
  .steps-intro{position:absolute;left:18px;top:100px;width:95px;color:#fff3e2}
  .steps-art{position:absolute;left:18px;top:150px;width:105px;height:100px;background:linear-gradient(150deg,#f6a94a,#e07a12);border-radius:8px}
  .step-card{position:absolute;left:140px;top:20px;width:240px}
  .step-card .step-title .heading{font-size:11px}
  .step-card .step-num{background:#fff;color:var(--orange);font-size:14px;width:16px;height:19px}
  .step-card .sub-heading{font-family:"Roboto Condensed",Arial,sans-serif;font-weight:700;font-size:6.5px;margin-top:8px;text-transform:uppercase}
  .step-card .body-text{color:#fff5e8;margin-top:2px}
</style>
</head>
<body>
<main class="stage">

  <p class="view-label view-label--top">Inner page</p>

  <section class="spread spread--campaign">
    <article class="page page--campaign">
      <div class="step-title">
        <span class="step-num">2</span>
        <h2 class="heading">We prepare effective marketing campaigns to give your project great exposure</h2>
      </div>
      <p class="body-text">Our marketing packages are built to reach serious buyers quickly and keep your launch visible every day of the campaign. Here are the marketing packages we provide to maximise your exposure:</p>
      <h3 class="sub-heading">High Searchly Ranking</h3>
      <p class="body-text">With strong search ranking, buyers find your project first when they look for new launches online.</p>
      <p class="callout">In order to achieve that, we focus on two key areas: 1) Search Engine Optimisation 2) Paid Search Advertising</p>
      <p class="body-text">Through our dedicated SEO team, your project page is tuned to rank on the first page for the terms buyers use most. To prove our results, we show our current rankings for general and project specific search terms on the next page.</p>
      <div class="ribbon-art" role="img" aria-label="Illustration of colourful ribbons flowing into a smartphone"></div>
    </article>

    <article class="page page--results">
      <div class="results-band"><h2 class="heading">Searchly Search Results</h2></div>
      <table class="results-table">
        <caption>General Search Terms Targeting Our Portal (www.brightkeyhomes.sg)</caption>
        <tr><th>Search Terms</th><th>Avg Monthly Searches</th><th>BrightKeyHomes Ranking</th></tr>
        <tr><td>New Launch Condo</td><td>1,000</td><td>#1 – #3</td></tr>
        <tr><td>New Launch Property</td><td>400</td><td>#2 – #6</td></tr>
        <tr><td>New Launch Singapore</td><td>260</td><td>#2 – #4</td></tr>
      </table>
      <table class="results-table">
        <caption>Specific Search Terms Targeting Individual Project Webpage (www.brightkeyhomes.sg/your-project)</caption>
        <tr><th>Search Terms</th><th>Avg Monthly Searches</th><th>BrightKeyHomes Ranking</th></tr>
        <tr><td>Harbourview Towers</td><td>2,900</td><td>#2 – #5</td></tr>
        <tr><td>Lakeside @ Elmer</td><td>1,300</td><td>#3 – #7</td></tr>
        <tr><td>The Corallina</td><td>1,300</td><td>#2 – #7</td></tr>
      </table>
      <p class="results-note">* Ranking fluctuates and may be slightly different from time to time.</p>
      <p class="see-it">See It For Yourself -&gt; www.searchly.com.sg</p>
      <p class="body-text"><strong>EFFECTIVE FRIENDBOOK MARKETING</strong><br>Another very important platform when it comes to online marketing is Friendbook. Recognized as the most popular social media, with a growing number of users, it is more effective compared to traditional marketing methods.</p>
      <p class="body-text">Considering distribution of 100,000 flyers, it will easily cost you more than $10,000 for design, printing and distribution.</p>
    </article>
  </section>

  <article class="page page--cover">
    <header class="cover-head">
      <div class="brand"><span class="brand-mark"></span>brightkeyhomes.sg</div>
      <p class="brand-tagline">DISCOVER THE LATEST PROPERTY LAUNCHES TODAY</p>
    </header>
    <h1 class="heading cover-title">Get more for less</h1>
    <p class="cover-sub">With our effective marketing packages for property launches</p>
    <div class="cover-art" role="img" aria-label="Illustration of a hand holding a tablet surrounded by marketing icons"></div>
    <footer class="cover-contact">
      <span>Bright Key Homes LLP<br>18 Marina View #08-02, Singapore 018961</span>
      <span>+65 6123 4567<br>hello@brightkeyhomes.sg</span>
    </footer>
  </article>

  <p class="view-label view-label--cover">Cover page</p>

  <section class="spread spread--steps">
    <article class="page page--about">
      <div class="icon-grid">
        <div class="tile tile--target"><svg width="16" height="16" viewBox="0 0 16 16"><circle cx="8" cy="8" r="7" fill="#fff"/><circle cx="8" cy="8" r="4.5" fill="#e5473b"/><circle cx="8" cy="8" r="2" fill="#fff"/></svg>Target</div>
        <div class="tile tile--mobile"><svg width="12" height="18" viewBox="0 0 12 18"><rect x="1" y="1" width="10" height="16" rx="2" fill="#fff"/><rect x="2.5" y="3" width="7" height="10" fill="#3a9fd8"/></svg>Mobile</div>
        <div class="tile tile--idea"><svg width="12" height="18" viewBox="0 0 12 18"><circle cx="6" cy="7" r="5.5" fill="#f5c21b"/><rect x="3.5" y="12" width="5" height="4" fill="#555"/></svg>Idea</div>
        <div class="tile tile--schedule"><svg width="18" height="18" viewBox="0 0 18 18"><circle cx="9" cy="9" r="8" fill="#fff" stroke="#555" stroke-width="1.5"/><path d="M9 4v5l3 2" stroke="#555" stroke-width="1.5" fill="none"/></svg>Schedule</div>
        <div class="tile tile--planning"><svg width="18" height="16" viewBox="0 0 18 16"><rect x="1" y="2" width="16" height="13" fill="#fff"/><rect x="1" y="2" width="16" height="3" fill="#e5473b"/></svg>Planning</div>
        <div class="tile tile--growth"><svg width="18" height="14" viewBox="0 0 18 14"><rect x="1" y="9" width="3" height="5" fill="#fff"/><rect x="6" y="6" width="3" height="8" fill="#fff"/><rect x="11" y="3" width="3" height="11" fill="#fff"/><rect x="15" y="0" width="2.5" height="14" fill="#e5473b"/></svg>Growth</div>
      </div>
      <div class="about-block">
        <h2 class="heading">About <span class="tag tag--green">Who we are</span></h2>
        <p class="body-text">BrightKeyHomes is an online portal focused on new property launches, helping developers and agencies reach active buyers.</p>
      </div>
      <div class="how-block">
        <h2 class="heading">How <span class="tag tag--orange">We work</span></h2>
        <p class="body-text">We combine a dedicated project webpage with search and social campaigns so your launch gets seen by the right audience.</p>
      </div>
    </article>

    <article class="page page--steps">
      <h2 class="heading steps-title">In 3 simple steps</h2>
      <p class="body-text steps-intro">We make marketing your new launch simple, effective and affordable.</p>
      <div class="steps-art" role="img" aria-label="Illustration of a laptop showing a project webpage"></div>
      <div class="step-card">
        <div class="step-title">
          <span class="step-num">1</span>
          <h3 class="heading">We create a full-featured webpage for your project</h3>
        </div>
        <h4 class="sub-heading">Good image</h4>
        <p class="body-text">A well designed project page gives buyers every key detail and makes a strong first impression.</p>
        <h4 class="sub-heading">We do it all for you</h4>
        <p class="body-text">Our team prepares the content, photos and floor plans so you can focus on sales.</p>
        <h4 class="sub-heading">One source of trusted information</h4>
        <p class="body-text">Buyers get accurate project facts in one place, building trust and bringing more enquiries.</p>
      </div>
    </article>
  </section>

  <p class="view-label view-label--bottom">Inner page</p>

</main>
</body>
</html>
```